Business Card Design Project

We have a logo design and are now looking for a business card design. We supply pre-construction services to the Wireless Telecommunication Industry in the development of cell phone tower and other antenna supporting infrastructure e.g. buildings. The types of services include Real Estate Leasing, Zoning & Permitting,Surveying and A&E work. I am looking for a card that includes the logo we have selected along with the full company name. Company colors are Blue and Silver. I want something professional and that "pops". Use your imagination with the four sided star portion of the logo - it can be stretched such that it occupies a large portion of the card or kept simple the way it is. I am interested in seeing the design on a white, silver, navy, black or charcoal background or any other color you think works well with the logo. Apart from the logo that includes LNI we also need to see the full company name on the card - Lanternway Networks, Inc. The design must also show a persons name, title, address, (2) phone numbers, e-mail address and web address www.lni-sample.co

Target Market(s)

Cell phone carriers e.g. Coravent Mobile, QB&R, K-Cellix, Dunmo etc.

Industry/Entity Type

Cell Phone

Requirements
Must have
• Logo and
Lanternway Networks, Inc.

```html
<!DOCTYPE html>
<html lang="en">
<head>
<meta charset="utf-8">
<title>Lanternway Networks – Business Cards</title>
<link href="https://fonts.googleapis.com/css2?family=Open+Sans:wght@400;600;700&family=Arimo:wght@400&family=Tinos:wght@700&display=swap" rel="stylesheet">
<style>
  :root{
    --bg:#e9e7e4;
    --charcoal:#252325;
    --black:#050505;
    --blue:#1f8fe0;
    --silver:#c9cacc;
    --silver-dark:#8e9093;
    --white:#ffffff;
  }
  html,body{margin:0;padding:0;overflow:hidden;}
  body{width:1200px;height:786px;background:var(--bg);position:relative;font-family:"Open Sans",sans-serif;}
  .card{position:absolute;width:540px;height:310px;box-shadow:0 10px 24px rgba(0,0,0,.28);overflow:hidden;color:var(--white);}
  .card--front{left:50px;top:70px;background:var(--charcoal);}
  .card--back-black{left:620px;top:60px;background:var(--black);}
  .card--back-charcoal{left:250px;top:420px;background:var(--charcoal);}

  .brand{position:absolute;left:0;right:0;top:46px;display:flex;justify-content:center;align-items:center;gap:14px;}
  .brand__dot{width:26px;height:26px;border-radius:50%;background:var(--blue);}
  .brand__name{font-family:"Open Sans",sans-serif;font-weight:700;font-size:64px;line-height:1;color:var(--blue);letter-spacing:2px;}
  .card--front .brand{top:34px;}
  .card--front .brand__name{font-size:56px;}

  .person{position:absolute;left:0;right:0;top:150px;text-align:center;font-size:18px;}
  .person__name{font-weight:700;}
  .contacts{position:absolute;left:0;right:0;top:184px;text-align:center;font-size:14px;line-height:26px;}
  .contacts__row{display:flex;justify-content:center;gap:22px;}
  .contact{display:inline-flex;align-items:center;gap:6px;}
  .contact svg{width:13px;height:13px;fill:var(--white);}

  .bands{position:absolute;left:0;top:236px;width:540px;height:22px;}
  .company{position:absolute;left:0;right:0;top:262px;text-align:center;font-size:12.5px;line-height:17px;}

  .tagline{position:absolute;left:0;right:0;top:152px;text-align:center;font-family:"Arimo",sans-serif;font-size:16px;letter-spacing:2.2px;line-height:19px;}
  .web{position:absolute;left:0;right:0;top:232px;text-align:center;font-family:"Tinos",serif;font-weight:700;font-size:16px;letter-spacing:3px;}
</style>
</head>
<body>

<section class="card card--front">
  <div class="brand"><span class="brand__dot"></span><span class="brand__name">LNI</span></div>
  <div class="person"><span class="person__name">Your Name,</span> Title</div>
  <div class="contacts">
    <div class="contacts__row">
      <span class="contact"><svg viewBox="0 0 16 16"><path d="M3 1l3 3-1.5 2a9 9 0 005.5 5.5L12 10l3 3-2 2C6 15 1 10 1 3z"/></svg>555-014-2763</span>
      <span class="contact"><svg viewBox="0 0 16 16"><path d="M4 1h7v4H4zM1 6h14v6h-3v3H4v-3H1zM5 10v4h6v-4z"/></svg>555-019-4821</span>
    </div>
    <div class="contacts__row">
      <span class="contact"><svg viewBox="0 0 16 16"><path d="M1 4h14v9H1zM2 5l6 4 6-4v-.5H2z" fill-rule="evenodd"/></svg>support@lni-sample.co</span>
      <span class="contact"><svg viewBox="0 0 16 16"><path d="M8 1a7 7 0 100 14A7 7 0 008 1zm0 1.5c1 1.2 1.6 3 1.7 4.8H6.3C6.4 5.5 7 3.7 8 2.5zM2.6 7.3h2.3c.1 1.8.6 3.4 1.4 4.6A5.5 5.5 0 012.6 7.3zm0 1.4zM8 13.5c-1-1.2-1.6-3-1.7-4.8h3.4C9.6 10.5 9 12.3 8 13.5zm1.7-1.6c.8-1.2 1.3-2.8 1.4-4.6h2.3a5.5 5.5 0 01-3.7 4.6z"/></svg>www.lni-sample.co</span>
    </div>
  </div>
  <svg class="bands" viewBox="0 0 540 22" aria-hidden="true">
    <polygon points="0,12 282,12 276,20 0,20" fill="var(--silver)"/>
    <polygon points="294,10 300,2 540,2 540,10" fill="var(--silver-dark)"/>
  </svg>
  <div class="company">Lanternway Networks, Inc.<br>4180 Harbor Vale Lane Fairview, Texas 70000-0000</div>
</section>

<section class="card card--back-black">
  <div class="brand"><span class="brand__dot"></span><span class="brand__name">LNI</span></div>
  <p class="tagline">LNI keeps you ahead of the competition<br>with fast and accurate execution of all<br>aspects of site acquisition.</p>
  <div class="web">www.lni-sample.co</div>
</section>

<section class="card card--back-charcoal">
  <div class="brand"><span class="brand__dot"></span><span class="brand__name">LNI</span></div>
  <p class="tagline">LNI keeps you ahead of the competition<br>with fast and accurate execution of all<br>aspects of site acquisition.</p>
  <div class="web">www.lni-sample.co</div>
</section>

</body>
</html>
```